Tolvik cards

I want a simple business card that pops.
Logo on one side.
On side two i want.
"Are you thinking about a new building on your property, or renovating an existing structure? Contact".....
Owners Name: Gary Pellman
Owners Phone number: 555-209-4176
Address:4716 Copper Fern RD, Halston, OH 43907
Committed to Quality, Service, and Integrity

```html
<!DOCTYPE html>
<html lang="en">
<head>
<meta charset="utf-8">
<title>Tolvik Builders – Business Card</title>
<link rel="stylesheet" href="https://fonts.googleapis.com/css2?family=Montserrat:wght@400;600;700;800&display=swap">
<style>
  :root {
    --backdrop: #ecebe8;
    --brown-deep: #4b2d19;
    --brown-mid: #7d6249;
    --brown-light: #a9977f;
    --brown-back: #422d1c;
    --white: #ffffff;
  }
  * { margin: 0; padding: 0; box-sizing: border-box; }
  html, body {
    width: 1181px; height: 1200px; overflow: hidden;
    background: var(--backdrop);
    font-family: "Montserrat", Arial, sans-serif;
  }
  .canvas { position: relative; width: 1181px; height: 1200px; }
  .card {
    position: absolute; left: 217px; width: 751px; height: 429px; overflow: hidden;
    box-shadow: 0 3px 10px rgba(0,0,0,0.18);
  }
  .card--front {
    top: 124px;
    background: linear-gradient(90deg, var(--brown-deep) 12%, var(--brown-mid) 50%, var(--brown-light) 92%);
    color: var(--white);
  }
  .card--back { top: 655px; background: var(--brown-back); }
  .corner-shape { position: absolute; inset: 0; width: 751px; height: 429px; }
  .owner-name {
    position: absolute; left: 28px; top: 75px;
    font-size: 31px; font-weight: 700; letter-spacing: 0.3px;
  }
  .tagline {
    position: absolute; left: 28px; top: 124px;
    font-size: 15px; font-weight: 600; line-height: 22px;
  }
  .tagline-rule {
    display: inline-block; width: 156px; height: 1.5px; background: var(--white);
    vertical-align: middle; margin-left: 4px;
  }
  .contact-row {
    position: absolute; left: 28px; display: flex; align-items: flex-start;
    font-size: 21px; font-weight: 400; line-height: 29px;
  }
  .contact-row--phone { top: 197px; }
  .contact-row--address { top: 234px; }
  .contact-icon { width: 26px; height: 26px; margin: 2px 14px 0 0; flex: none; }
  .pitch {
    position: absolute; left: 28px; top: 316px; width: 500px;
    font-size: 19px; line-height: 25px; font-weight: 400;
  }
  .brand-name {
    position: absolute; left: 639px; top: 230px; transform: translate(-50%, -50%);
    display: flex; align-items: center; gap: 10px;
    color: var(--brown-deep); font-size: 40px; font-weight: 800; letter-spacing: 0.5px;
  }
  .brand-mark { width: 16px; height: 16px; background: var(--brown-deep); }
  .brand-name--back {
    left: 375px; top: 214px; color: var(--white); font-size: 64px;
  }
  .brand-name--back .brand-mark { width: 24px; height: 24px; background: var(--white); }
</style>
</head>
<body>
<main class="canvas">
  <section class="card card--front" aria-label="Business card front">
    <svg class="corner-shape" viewBox="0 0 636 363" preserveAspectRatio="none" aria-hidden="true">
      <polygon points="538,0 368,181 592,363 636,363 636,0" fill="var(--brown-deep)"/>
      <polygon points="588,0 398,181 636,352 636,0" fill="var(--white)"/>
    </svg>
    <h1 class="owner-name">GARY PELLMAN</h1>
    <p class="tagline">Committed to Quality, Service,<br>and Integrity<span class="tagline-rule"></span></p>
    <div class="contact-row contact-row--phone">
      <svg class="contact-icon" viewBox="0 0 24 24" aria-hidden="true">
        <circle cx="12" cy="12" r="12" fill="var(--white)"/>
        <path d="M8.2 6.2l2 2.1c.3.3.3.8 0 1.1l-1 1c.8 1.7 2 2.9 3.6 3.7l1-1c.3-.3.8-.3 1.1 0l2 2c.3.3.3.8 0 1.1l-1.1 1.1c-.6.6-1.5.7-2.2.3-3-1.6-5.300-3.9-6.9-6.9-.4-.7-.3-1.6.3-2.2L7.1 6.2c.3-.3.8-.3 1.1 0z" fill="var(--brown-deep)"/>
      </svg>
      <span>555-209-4176</span>
    </div>
    <div class="contact-row contact-row--address">
      <svg class="contact-icon" viewBox="0 0 24 24" aria-hidden="true">
        <circle cx="12" cy="12" r="12" fill="var(--white)"/>
        <path d="M12 4.5c-2.9 0-5 2.2-5 5 0 3.6 5 9.5 5 9.5s5-5.9 5-9.5c0-2.8-2.1-5-5-5zm0 7a2 2 0 1 1 0-4 2 2 0 0 1 0 4z" fill="var(--brown-deep)"/>
      </svg>
      <span>4716 Copper Fern RD, Halston,<br>OH 43907</span>
    </div>
    <p class="pitch">Are you thinking about a new building on your property, or renovating an existing structure? Contact</p>
    <div class="brand-name"><span class="brand-mark"></span>TOLVIK</div>
  </section>

  <section class="card card--back" aria-label="Business card back">
    <div class="brand-name brand-name--back"><span class="brand-mark"></span>TOLVIK</div>
  </section>
</main>
</body>
</html>
```